Announcement for a New Trauma Therapy Group - Rack Card

I need a two-sided "rack" card that is 4x9 announcing a Women's Trauma and Loss Group. I am a licensed therapist and will be starting this support group for women who have experienced trauma of all kinds. In addition to groups, I offer individual, couples, and family counseling sessions.

I would like to see designs that are soft tones and use colors like muted blues, greens, and sand tones. The final design should communicate hope and healing as well as have a peaceful feel to it.

I would like a picture of a woman's profile from either the side or from behind her. (possibly a contemplative picture on a beach)

I am attaching a picture of myself to go alongside the bio information as well.

On One Side, I need the description of the group and contact info:

Healing the Hurting Heart
Women's Trauma & Loss Group
Led by Licensed Professional Counselor, Joy Belden Crane

10 Week Group
Cost - $35 session
Group size limited to 10 participants

Topics Include:
What is Trauma?
How Trauma Affects Us
Creating a Feeling of Safety
Managing Trauma Triggers
Importance of Self Care
Healthy vs. Unhealthy Coping
Guilt, Shame, and Blame
Victim vs. Victimized
Grieving through Loss
Anger and Forgiveness
Imagining a Better Future

For More Information, Contact:
Joy Belden Crane, LPC, LMFT
(555) 614-3928
joy@brightmeadowcare.example

On Side Two:

Life hurts and does not seem fair. So what do you do when you are faced with an event in your life that knocks you off your feet? It seems no one understands what you are feeling and no one knows just what to say. It is tempting to pull away and isolate or put up a mask and pretend everything is OK.

It is my desire you know that you are not alone! There are others who understand the feelings you are going through and offer a safe place for encouraging support. I want to invite you to embark on a courageous journey of healing where you will not only learn how to "survive" after trauma and loss, but instead, learn that you can once again "thrive"!
- Joy Belden Crane, LPC, LMFT

Joy Belden Crane is a Licensed Professional Counselor and Licensed Marriage and Family Therapist. She is the owner of Still Waters Counseling Services located in Tulsa, OK.

Joy is a trauma survivor herself and understands firsthand the unique challenges that can arise on the journey to healing.

(Include Joy's picture next to bio)

(Attach logo and business information to this side as well.)

Target Market(s)

Women who have gone through a traumatic experience or loss and are hurting emotionally

Industry/Entity Type

Counsellor

Font styles to use
Serif
Script

Colors
fbe7d2
86cfc6
cfeae6
85abd2
cfdeed

Requirements
Must have
• Joy's picture as well as her logo and contact information must be on the card.
• One side of the card should describe the group with the following description:
• "Healing the Hurting Heart"
• Women's Trauma & Loss Group
• Led by Licensed Professional Counselor, Joy Belden Crane
• 10 Week Group
• Cost - $35 session
• Group size limited to 10 participants
• Topics Include:
• What is Trauma?
• How Trauma Affects Us
• Creating a Feeling of Safety
• Managing Trauma Triggers
• Importance of Self Care
• Healthy vs. Unhealthy Coping
• Guilt, Shame, and Blame
• Victim vs. Victimized
• Grieving through Loss
• Anger and Forgiveness
• Imagining a Better Future
• For More Information, Contact:
• Joy Belden Crane, LPC, LMFT
• (555) 614-3928
• joy@brightmeadowcare.example
• On the second side, it must have this note from Joy:
• Life hurts and does not seem fair. So what do you do when you are faced with an event in your life that knocks you off your feet? It seems no one understands what you are feeling and no one knows just what to say. It is tempting to pull away and isolate or put up a mask and pretend everything is OK.
• It is my desire you know that you are not alone! There are others who understand the feelings you are going through and offer a safe place for encouraging support. I want to invite you to embark on a courageous journey of healing where you will not only learn how to "survive" after trauma and loss, but instead, learn that you can once again "thrive"!
• - Joy Belden Crane, LPC, LMFT
• Joy Belden Crane is a Licensed Professional Counselor and Licensed Marriage and Family Therapist. She is the owner of Still Waters Counseling Services located in Tulsa, OK.
• Joy is a trauma survivor herself and understands firsthand the unique challenges that can arise on the journey to healing. In addition to facilitating groups, Joy also offers individual, marriage, and family counseling.
Nice to have
• soft muted colors that are peaceful. Light blues, greens, sand colors would work well. A picture at the top of the card of either a woman or a woman's profile that is hopeful such as a woman sitting at a beach overlooking the ocean.
Should not have
• No harsh or bright bold colors. This card needs to have a peaceful feeling to it.

```html
<!DOCTYPE html>
<html lang="en">
<head>
<meta charset="utf-8">
<title>Healing the Hurting Heart – Rack Card</title>
<link rel="stylesheet" href="https://fonts.googleapis.com/css2?family=Pinyon+Script&family=Roboto:wght@400&family=Roboto+Condensed:wght@400;700&family=Open+Sans:ital,wght@0,400;0,700;1,700&display=swap">
<style>
  :root {
    --backdrop: #707070;
    --leaf-green: #99d500;
    --leaf-green-deep: #5f9a1c;
    --ink: #111111;
    --paper: #ffffff;
    --sand-light: #c9b59c;
    --sand-mid: #a39078;
    --sand-dark: #7d6d5e;
  }
  * { margin: 0; padding: 0; box-sizing: border-box; }
  html, body { width: 1200px; height: 1200px; overflow: hidden; }
  body { background: var(--backdrop); position: relative; }

  .rack-card {
    position: absolute;
    left: 342px; top: 20px;
    width: 515px; height: 1160px;
    background: var(--paper);
    overflow: hidden;
  }
  .card-art { position: absolute; inset: 0; width: 515px; height: 1160px; }

  .title {
    position: absolute; left: 0; width: 100%;
    font-family: "Pinyon Script", cursive;
    color: var(--ink);
    font-size: 64px; line-height: 1;
  }
  .title-line-1 { top: 488px; text-align: center; padding-left: 30px; }
  .title-line-2 { top: 558px; text-align: center; padding-left: 30px; }

  .subtitle {
    position: absolute; top: 645px; left: 0; width: 100%;
    text-align: center;
    font-family: "Roboto", sans-serif; font-size: 17px; line-height: 22px;
    letter-spacing: 0.4px; color: var(--ink);
  }
  .duration {
    position: absolute; top: 725px; left: 0; width: 100%;
    text-align: center;
    font-family: "Roboto", sans-serif; font-size: 34px; color: var(--ink);
  }
  .cost {
    position: absolute; top: 765px; left: 0; width: 100%;
    text-align: center;
    font-family: "Roboto", sans-serif; font-size: 17px; color: var(--ink);
  }

  .topics-heading {
    position: absolute; top: 822px; left: 29px;
    font-family: "Roboto Condensed", sans-serif; font-weight: 700;
    font-size: 24px; color: var(--ink);
  }
  .topic-list {
    position: absolute; top: 865px; list-style: none;
    font-family: "Roboto Condensed", sans-serif; font-size: 17.5px;
    line-height: 21.6px; color: var(--ink);
  }
  .topic-list-left { left: 36px; }
  .topic-list-right { left: 294px; }
  .topic-list li { display: flex; align-items: center; gap: 6px; white-space: nowrap; }
  .tick { width: 11px; height: 11px; flex: none; }
  .topic-divider {
    position: absolute; left: 273px; top: 868px;
    width: 1px; height: 127px; background: var(--leaf-green-deep);
  }

  .practice-name {
    position: absolute; left: 30px; top: 1080px;
    display: flex; align-items: center; gap: 8px;
    font-family: "Open Sans", sans-serif; font-weight: 400;
    font-size: 17px; color: var(--leaf-green-deep);
    width: 200px; line-height: 21px;
  }
  .practice-mark {
    width: 26px; height: 26px; border-radius: 50%;
    background: var(--leaf-green); flex: none;
  }

  .contact {
    position: absolute; right: 28px; top: 1046px;
    text-align: right;
    font-family: "Open Sans", sans-serif; font-size: 14px;
    line-height: 25.5px; color: var(--ink);
  }
  .contact-heading { font-weight: 700; font-size: 15px; }
  .contact-strong { font-weight: 700; font-style: italic; }
</style>
</head>
<body>
  <article class="rack-card">
    <svg class="card-art" viewBox="0 0 515 1160" aria-hidden="false">
      <defs>
        <linearGradient id="beach-tones" x1="0" y1="0" x2="0" y2="1">
          <stop offset="0" stop-color="#b59a7c"/>
          <stop offset="0.25" stop-color="#a89a8c"/>
          <stop offset="0.7" stop-color="#8d7f72"/>
          <stop offset="1" stop-color="#a3957f"/>
        </linearGradient>
      </defs>
      <rect class="hero-photo" x="0" y="0" width="515" height="520" fill="url(#beach-tones)"
            role="img" aria-label="Photo of the counselor sitting on a rock on a sandy beach at sunset"/>
      <path class="green-panel" fill="var(--leaf-green)"
            d="M0 505 C60 470 110 440 190 440 C300 440 420 420 515 385 L515 1160 L0 1160 Z"/>
      <path class="footer-panel" fill="var(--paper)"
            d="M0 1024 C120 1010 200 1005 300 1000 C400 995 460 990 515 988 L515 1160 L0 1160 Z"/>
    </svg>

    <h1>
      <span class="title title-line-1">Healing the</span>
      <span class="title title-line-2">Hurting Heart</span>
    </h1>

    <p class="subtitle">Women's Trauma &amp; Loss Group Led by<br>Licensed Professional Counselor, Joy Belden Crane</p>
    <p class="duration">10 WEEK GROUP</p>
    <p class="cost">Cost - $35 session Group size limited to 10 participants</p>

    <h2 class="topics-heading">Topics Include</h2>
    <ul class="topic-list topic-list-left">
      <li><svg class="tick" viewBox="0 0 12 12"><path d="M1 6.5 L4.5 10 L11 2" fill="none" stroke="var(--ink)" stroke-width="2.2"/></svg>What is Trauma?</li>
      <li><svg class="tick" viewBox="0 0 12 12"><path d="M1 6.5 L4.5 10 L11 2" fill="none" stroke="var(--ink)" stroke-width="2.2"/></svg>How Trauma Affects Us</li>
      <li><svg class="tick" viewBox="0 0 12 12"><path d="M1 6.5 L4.5 10 L11 2" fill="none" stroke="var(--ink)" stroke-width="2.2"/></svg>Creating a Feeling of Safety</li>
      <li><svg class="tick" viewBox="0 0 12 12"><path d="M1 6.5 L4.5 10 L11 2" fill="none" stroke="var(--ink)" stroke-width="2.2"/></svg>Managing Trauma Triggers</li>
      <li><svg class="tick" viewBox="0 0 12 12"><path d="M1 6.5 L4.5 10 L11 2" fill="none" stroke="var(--ink)" stroke-width="2.2"/></svg>Importance of Self Care</li>
      <li><svg class="tick" viewBox="0 0 12 12"><path d="M1 6.5 L4.5 10 L11 2" fill="none" stroke="var(--ink)" stroke-width="2.2"/></svg>Healthy vs. Unhealthy Coping</li>
    </ul>
    <div class="topic-divider"></div>
    <ul class="topic-list topic-list-right">
      <li><svg class="tick" viewBox="0 0 12 12"><path d="M1 6.5 L4.5 10 L11 2" fill="none" stroke="var(--ink)" stroke-width="2.2"/></svg>Guilt, Shame, and Blame</li>
      <li><svg class="tick" viewBox="0 0 12 12"><path d="M1 6.5 L4.5 10 L11 2" fill="none" stroke="var(--ink)" stroke-width="2.2"/></svg>Victim vs. Victimized</li>
      <li><svg class="tick" viewBox="0 0 12 12"><path d="M1 6.5 L4.5 10 L11 2" fill="none" stroke="var(--ink)" stroke-width="2.2"/></svg>Grieving through Loss</li>
      <li><svg class="tick" viewBox="0 0 12 12"><path d="M1 6.5 L4.5 10 L11 2" fill="none" stroke="var(--ink)" stroke-width="2.2"/></svg>Anger and Forgiveness</li>
      <li><svg class="tick" viewBox="0 0 12 12"><path d="M1 6.5 L4.5 10 L11 2" fill="none" stroke="var(--ink)" stroke-width="2.2"/></svg>Imagining a Better Future</li>
    </ul>

    <div class="practice-name">
      <span class="practice-mark"></span>
      <span>Still Waters Counseling</span>
    </div>

    <address class="contact" style="font-style:normal">
      <div class="contact-heading">For More Information, Contact</div>
      <div>Joy Belden Crane, LPC, LMFT</div>
      <div class="contact-strong">(555) 614-3928</div>
      <div class="contact-strong">joy@brightmeadowcare.example</div>
    </address>
  </article>
</body>
</html>
```